Young, funky marketing collateral and other stuff
Exciting and innovative ideas welcomed
We are thrilled with the designs that have come in and are now spoilt for choice as they are all individually very good. We appreciate the trouble you have gone to in response to our direct feedback as we 'fine tune' our ideas. Thanks designers, you are all great.
A big thank you also to Owen in Support who has helped to smooth the way between us and the designers when we have run into difficulty conveying some of our ideas.
Have already recommended Tallowspan to others
Regards
RTolley
Fernwick logo
#14: the way that the fernwick logo colours have been made neutral is very good and perfectly acceptable to us.
A general reminder; fernwick logo only on biz card, folder, letterhead and signature. Not on other things.
Address Label:
#13 has the right idea for the address label, however we would like it to be landscape design rather than portrait
Yard signs: it would be good to have the branding colours 'frame' the signs in some way too thanks. Thanks for your great efforts.
Hi Designers
On the yard signs, please include as part of the branding template:
www.kvtp.co.nz
Thanks
Clarification on Registry. Please use the following 'Open for Inspection Registry' not 'Open House Registry'. Thanks.
Also, the Registry does not require fernwick logo.
Brightnook, thanks for your ideas. #4 is attractive, we prefer the way you have presented the company address in the letterhead, by contrast in #3 the company address in footer looks a bit staggered and not so smart. The logo reflection on the #4 folder is also very appealing.
#5 Thank you for your new design.
The address label; please make the dot dot lines in the receiver's address longer and more central. We will be handwriting the receiver's address on the dot dot line and it needs to have enough space to do this and so that a courier or post office can read the address and deliver the package easily.
Thanks for the new designs. I can see that trying to incorporate the 2nd logo (fernwick property) is simply going to cause confusion however we do need somehow to represent the second company. Instead of using logo, please just use company name and designation which is 'Fernwick Property Ltd, Licensed Agent (PLNB) 2008. Please include this on the business card, folder, letterhead, and signature. It would be suitable to have it, for instance, in the bottom line of the footer, the two company names as bullet points.
@DW - please check your private message on top right corner after clicking messages once you log in. Thanks
A big thanks to pixvellor for starting of the process with neat designs #1 and #2.
My brief may not have been totally clear so here are a couple more thoughts:
The mailing label: There needs to be a space (........... line) after 'company/name etc so that the sender can hand write the details in. For example:
Company/Name ...........................................
Address .................................................
.........................................................City ....................................................
Phone ...................................................
Attention ...............................................
Please also note my comment at start of brief about also including Fernwick property details on some of the collateral. If it's going to look too crowded, just use the fernwick logo.
On the 'inspect today' sign, the 'inspect today' plus arrow are major components, the branding is minor. This sign will be placed at intersections directing buyers to a home, so the size of the arrow is important.
Thanks everyone and we look forward to seeing your ideas.

```html
<!DOCTYPE html>
<html lang="en">
<head>
<meta charset="utf-8">
<title>Halvern Realty – Collateral Set</title>
<link rel="stylesheet" href="https://fonts.googleapis.com/css2?family=Roboto:wght@400;500;700&display=swap">
<style>
  :root {
    --blue: #1a8fd8;
    --blue-deep: #0b5fa8;
    --blue-pale: #cfeaf9;
    --ink: #1d2a36;
    --grey: #8a96a3;
    --paper: #ffffff;
    --label: #555f69;
  }
  * { box-sizing: border-box; margin: 0; padding: 0; }
  html, body { width: 1200px; height: 365px; overflow: hidden; background: var(--paper); }
  body { position: relative; font-family: "Roboto", Arial, sans-serif; color: var(--ink); }

  .piece { position: absolute; background: var(--paper); overflow: hidden; box-shadow: 0 0 0 1px #dde3e8; }
  .piece-label { position: absolute; font-size: 7px; color: var(--label); font-weight: 500; }
  .swoosh { position: absolute; left: 0; width: 100%; display: block; }

  .brand { display: flex; align-items: center; gap: 5px; font-weight: 700; color: var(--blue-deep); white-space: nowrap; }
  .brand-mark { background: var(--blue); display: inline-block; }

  /* Pocket folder */
  .folder { left: 12px; top: 19px; width: 396px; height: 282px; }
  .folder-panel { position: absolute; top: 0; height: 100%; width: 50%; }
  .folder-panel.right { left: 50%; border-left: 1px solid #e3e8ec; }
  .folder-card { position: absolute; left: 26px; top: 28px; width: 74px; height: 70px; border: 1px solid #d7e3ec; background: #f4f9fc; padding: 8px 6px; }
  .folder-card .brand { font-size: 6px; gap: 3px; }
  .folder-card .brand-mark { width: 9px; height: 9px; }
  .folder-card p { font-size: 3.5px; color: var(--grey); margin-top: 5px; line-height: 1.5; }
  .folder-panel.right .brand { position: absolute; left: 36px; top: 140px; font-size: 15px; }
  .folder-panel.right .brand-mark { width: 20px; height: 20px; }
  .folder-url { position: absolute; left: 0; right: 0; top: 210px; text-align: center; font-size: 5px; color: var(--grey); }
  .pocket { position: absolute; left: 12px; top: 300px; width: 396px; height: 60px; background: linear-gradient(180deg, var(--blue) 0%, #61b9ea 100%); }
  .pocket-slot { position: absolute; left: 40px; top: 16px; width: 52px; height: 30px; background: var(--blue-deep); border: 1px solid #8fd0f3; }
  .pocket-slot .brand { color: var(--paper); font-size: 4px; margin: 10px 0 0 6px; gap: 2px; }
  .pocket-slot .brand-mark { width: 5px; height: 5px; background: var(--paper); }

  /* Letterhead */
  .letterhead { left: 427px; top: 19px; width: 137px; height: 221px; }
  .letterhead .brand { position: absolute; left: 10px; top: 32px; font-size: 7px; gap: 3px; }
  .letterhead .brand-mark { width: 10px; height: 10px; }
  .lh-lines { position: absolute; left: 10px; right: 12px; top: 70px; }
  .lh-lines span { display: block; height: 2px; background: #e6ebef; margin-bottom: 7px; }

  /* Business cards */
  .card { left: 569px; width: 98px; height: 48px; }
  .card .brand { position: absolute; left: 8px; top: 16px; font-size: 6px; gap: 3px; }
  .card .brand-mark { width: 8px; height: 8px; }
  .card-detail { position: absolute; left: 8px; bottom: 10px; font-size: 3.5px; color: var(--grey); line-height: 1.4; }

  /* Signature */
  .signature { left: 427px; top: 271px; width: 240px; height: 53px; }
  .signature .brand { position: absolute; left: 10px; top: 20px; font-size: 8px; gap: 3px; }
  .signature .brand-mark { width: 10px; height: 10px; }
  .sig-text { position: absolute; left: 120px; top: 14px; font-size: 5px; color: var(--grey); line-height: 1.5; }
  .sig-text strong { color: var(--ink); font-weight: 700; }

  /* Registry sign */
  .sign { left: 672px; top: 10px; width: 524px; height: 350px; }
  .sign-tagline { position: absolute; right: 14px; top: 6px; font-size: 12px; color: var(--paper); }
  .sign .brand { position: absolute; left: 130px; top: 86px; font-size: 32px; }
  .sign .brand-mark { width: 42px; height: 42px; }
  .sign-title { position: absolute; left: 0; right: 0; top: 214px; text-align: center; font-size: 27px; font-weight: 700; color: var(--ink); }
  .sign-subtitle { position: absolute; left: 0; right: 0; top: 248px; text-align: center; font-size: 21px; color: var(--ink); }
  .sign-url { position: absolute; left: 0; right: 0; top: 295px; text-align: center; font-size: 12px; color: var(--grey); }
</style>
</head>
<body>

<span class="piece-label" style="left:12px;top:8px">Pocket Folder</span>
<section class="piece folder">
  <div class="folder-panel left">
    <div class="folder-card">
      <div class="brand"><span class="brand-mark"></span>HALVERN REALTY</div>
      <p>Fernwick Property Ltd<br>Licensed Agent (PLNB) 2008</p>
    </div>
  </div>
  <div class="folder-panel right">
    <div class="brand"><span class="brand-mark"></span>HALVERN REALTY</div>
    <div class="folder-url">www.kvtp.co.nz</div>
  </div>
  <svg class="swoosh" style="bottom:0;height:70px" viewBox="0 0 400 70" preserveAspectRatio="none">
    <path d="M0 30 C120 70 260 -10 400 20 L400 70 L0 70Z" fill="var(--blue-pale)"/>
    <path d="M0 45 C140 75 250 10 400 35 L400 70 L0 70Z" fill="var(--blue)"/>
    <path d="M0 58 C150 80 260 30 400 52 L400 70 L0 70Z" fill="var(--blue-deep)"/>
  </svg>
</section>
<div class="pocket">
  <div class="pocket-slot"><div class="brand"><span class="brand-mark"></span>HALVERN</div></div>
</div>

<span class="piece-label" style="left:427px;top:8px">Letter Head</span>
<section class="piece letterhead">
  <svg class="swoosh" style="top:0;height:28px" viewBox="0 0 140 28" preserveAspectRatio="none">
    <path d="M0 0 L140 0 L140 10 C90 26 40 4 0 18Z" fill="var(--blue)"/>
    <path d="M0 18 C40 4 90 26 140 10 L140 14 C90 30 40 9 0 22Z" fill="var(--blue-pale)"/>
  </svg>
  <div class="brand"><span class="brand-mark"></span>HALVERN REALTY</div>
  <div class="lh-lines"><span></span><span></span><span></span><span></span><span></span><span></span><span></span><span></span></div>
  <svg class="swoosh" style="bottom:0;height:26px" viewBox="0 0 140 26" preserveAspectRatio="none">
    <path d="M0 10 C50 24 100 0 140 8 L140 26 L0 26Z" fill="var(--blue)"/>
  </svg>
</section>

<span class="piece-label" style="left:612px;top:20px">Biz Card Front</span>
<section class="piece card" style="top:29px">
  <svg class="swoosh" style="bottom:0;height:18px" viewBox="0 0 100 18" preserveAspectRatio="none">
    <path d="M0 8 C40 18 70 0 100 6 L100 18 L0 18Z" fill="var(--blue)"/>
  </svg>
  <div class="brand"><span class="brand-mark"></span>HALVERN REALTY</div>
</section>
<span class="piece-label" style="left:612px;top:78px">Biz Card Back</span>
<section class="piece card" style="top:87px">
  <svg class="swoosh" style="top:0;height:12px" viewBox="0 0 100 12" preserveAspectRatio="none">
    <path d="M0 0 L100 0 L100 4 C60 12 30 2 0 8Z" fill="var(--blue)"/>
  </svg>
  <div class="card-detail">Jane Harlow · Sales Consultant<br>021 555 0148 · www.kvtp.co.nz</div>
</section>
<section class="piece card" style="top:144px">
  <svg class="swoosh" style="bottom:0;height:14px" viewBox="0 0 100 14" preserveAspectRatio="none">
    <path d="M0 6 C40 14 70 0 100 4 L100 14 L0 14Z" fill="var(--blue)"/>
  </svg>
  <div class="brand"><span class="brand-mark"></span>HALVERN REALTY</div>
</section>

<span class="piece-label" style="left:427px;top:261px">Signature</span>
<section class="piece signature">
  <div class="brand"><span class="brand-mark"></span>HALVERN REALTY</div>
  <div class="sig-text"><strong>Jane Harlow</strong><br>Sales Consultant · 021 555 0148<br>Fernwick Property Ltd, Licensed Agent (PLNB) 2008</div>
  <svg class="swoosh" style="bottom:0;height:10px" viewBox="0 0 240 10" preserveAspectRatio="none">
    <path d="M0 4 C80 10 160 0 240 3 L240 10 L0 10Z" fill="var(--blue)"/>
  </svg>
</section>

<span class="piece-label" style="left:672px;top:0">Sign</span>
<section class="piece sign">
  <svg class="swoosh" style="top:0;height:80px" viewBox="0 0 524 80" preserveAspectRatio="none">
    <path d="M0 0 L524 0 L524 26 L200 26 C120 26 60 50 0 78Z" fill="var(--blue)"/>
    <path d="M0 78 C60 50 120 26 200 26 L524 26 L524 30 L210 30 C130 30 70 56 0 80Z" fill="var(--blue-pale)"/>
  </svg>
  <div class="sign-tagline">Save thousands in commission</div>
  <div class="brand"><span class="brand-mark"></span>HALVERN REALTY</div>
  <div class="sign-title">Seller Requests Registration</div>
  <div class="sign-subtitle">Open for inspection registry</div>
  <div class="sign-url">www.kvtp.co.nz</div>
  <svg class="swoosh" style="bottom:0;height:40px" viewBox="0 0 524 40" preserveAspectRatio="none">
    <path d="M0 14 C180 40 340 0 524 18 L524 40 L0 40Z" fill="var(--blue-pale)"/>
    <path d="M0 24 C180 44 340 10 524 28 L524 40 L0 40Z" fill="var(--blue)"/>
  </svg>
</section>

</body>
</html>
```